Tarvel Works - Powerpoint Templates

We are a consultancy to help builders to optimize their planning in order to save building costs. For that reason we need templates for teasers and presentations where we offer our services, show our team and their capacities and present workflows, organization charts, price lists etc.

```html
<!DOCTYPE html>
<html lang="en">
<head>
<meta charset="utf-8">
<title>Tarvel Works – Presentation Template</title>
<link href="https://fonts.googleapis.com/css2?family=Open+Sans:wght@400;600;700;800&family=Arimo:wght@400;700&display=swap" rel="stylesheet">
<style>
:root{
  --gold:#b9862f;
  --gold-light:#e0b766;
  --gold-muted:#d9ad62;
  --black:#000;
  --ink:#222;
  --body:#555;
  --page:#fff;
  --cream:#f7e6c4;
}
*{box-sizing:border-box;margin:0;padding:0}
html,body{width:1200px;height:4199px;overflow:hidden;background:var(--page)}
body{position:relative;font-family:"Arimo",Arial,sans-serif;color:var(--ink)}
.slide{position:absolute;left:23px;width:1149px;height:647px;background:#fff;box-shadow:0 0 6px rgba(0,0,0,.18);overflow:hidden}
.abs{position:absolute}
.brand{font-family:"Open Sans",sans-serif;font-weight:800;color:var(--gold);letter-spacing:.04em;text-transform:uppercase;white-space:nowrap}
.header{position:absolute;left:0;top:0;width:1149px;height:56px}
.header h2{position:absolute;left:23px;top:10px;font-family:"Open Sans",sans-serif;font-weight:700;font-size:30px;color:#fff;letter-spacing:.01em}
.header .brand{position:absolute;left:975px;top:18px;font-size:15px}
.copyright{position:absolute;left:18px;bottom:18px;font-size:14px;color:#333}
.page-no{position:absolute;right:18px;bottom:14px;font-size:18px;color:#222}
/* hero */
.hero-photo{position:absolute;inset:0;background:linear-gradient(135deg,#1d2a3c 0%,#4b607a 35%,#2b3544 60%,#6a5a48 100%)}
.hero-pill{position:absolute;left:229px;top:83px;width:680px;height:167px;border-radius:84px;background:var(--black);display:flex;align-items:center;justify-content:center}
.hero-pill .brand{font-size:56px}
/* about */
.about-tab{left:92px;top:112px;width:350px;height:60px;border-radius:24px 24px 0 0;background:var(--gold)}
.about-mark{left:47px;top:150px;width:441px;height:427px;background:#fff;border-radius:18px;box-shadow:0 0 8px rgba(0,0,0,.25);display:flex;align-items:center;justify-content:center}
.about-mark .brand{font-size:44px}
.about-text{left:546px;top:180px;width:546px;font-size:12.6px;line-height:25px;color:var(--body);text-align:justify}
/* services */
.service{position:absolute;top:90px;width:263px;height:437px;border-radius:132px 132px 0 0;text-align:center;overflow:hidden}
.service.dark{background:var(--black)}
.service.gold{background:var(--gold)}
.service .brand{display:block;margin-top:40px;font-size:15px}
.service.gold .brand{color:#fff}
.service h3{margin-top:36px;font-family:"Open Sans",sans-serif;font-weight:700;font-size:17px}
.service.dark h3{color:var(--gold)}
.service.gold h3{color:var(--gold-muted)}
.service p{margin:20px 18px 0;font-size:12.6px;line-height:20.5px;color:#fff}
.service .go{position:absolute;left:83px;bottom:-48px;width:96px;height:96px;border-radius:50%}
.service.dark .go{background:var(--gold)}
.service.gold .go{background:var(--black)}
.service .go svg{position:absolute;left:36px;top:12px}
/* capacities */
.cap-icon{position:absolute;width:74px;height:74px;border-radius:50%;background:var(--gold)}
.cap-icon svg{position:absolute;left:19px;top:19px}
.cap-item{position:absolute;width:260px}
.cap-item h4{font-family:"Open Sans",sans-serif;font-weight:700;font-size:14px;line-height:18px;color:#111}
.cap-item p{margin-top:10px;font-size:9px;line-height:13px;color:#444}
.cap-center{left:475px;top:280px;width:200px;text-align:center}
.cap-center .brand{font-size:24px}
/* team */
.member{position:absolute;top:168px;width:317px;height:411px;text-align:center}
.member.gold{background:var(--gold)}
.member.dark{background:var(--black)}
.member .photo{position:absolute;left:64px;top:-65px;width:188px;height:188px;border-radius:50%;border:4px solid #fff;background:linear-gradient(160deg,#d9d4cc,#8c8b86)}
.member h3{position:absolute;left:0;right:0;top:163px;font-family:"Open Sans",sans-serif;font-weight:600;font-size:27px;color:#fff}
.member p{position:absolute;left:22px;right:22px;top:228px;font-family:"Open Sans",sans-serif;font-size:20px;line-height:28px}
.member.gold p{color:var(--cream)}
.member.dark p{color:#fff}
/* thank you */
.closing-photo{position:absolute;inset:0;background:linear-gradient(160deg,#1a1a1a,#0c0c0c 60%,#262320)}
.closing-brand{left:0;right:0;top:80px;text-align:center}
.closing-brand .brand{font-size:56px}
.thanks-box{left:174px;top:226px;width:797px;height:340px;background:var(--gold)}
.thanks-box h2{position:absolute;left:0;right:0;top:42px;text-align:center;font-family:"Open Sans",sans-serif;font-weight:700;font-size:80px;color:#fff;letter-spacing:.01em}
.contact{position:absolute;top:163px;width:220px;text-align:center;color:#fff;font-size:14px;line-height:17px}
.contact .ring{width:72px;height:72px;border-radius:50%;border:2px solid #fff;margin:0 auto 14px;display:flex;align-items:center;justify-content:center}
.closing .copyright,.closing .page-no{color:#fff}
.closing .page-no{font-weight:700}
</style>
</head>
<body>

<!-- Cover -->
<section class="slide" style="top:23px">
  <div class="hero-photo" role="img" aria-label="Business team meeting in a glass-walled office"></div>
  <div class="hero-pill"><span class="brand">Tarvel Works</span></div>
</section>

<!-- About -->
<section class="slide" style="top:712px">
  <div class="header">
    <svg width="1149" height="56" viewBox="0 0 1149 56"><polygon points="0,0 935,0 900,56 0,56" fill="#000"/><polygon points="947,0 960,0 925,56 912,56" fill="#b9862f"/><polygon points="968,0 981,0 946,56 933,56" fill="#b9862f"/></svg>
    <h2>ABOUT US</h2><span class="brand">Tarvel Works</span>
  </div>
  <div class="abs about-tab"></div>
  <div class="abs about-mark"><span class="brand">Tarvel Works</span></div>
  <p class="abs about-text">Sed ut perspiciatis unde omnis iste natus error sit voluptatem accusantium doloremque lau dantium, totam rem aperiam, eaque ipsa quae ab illo inventore veritatis et quasi architecto beatae vitae dicta sunt explicabo. Nemo enim ipsam voluptatem quia voluptas sit aspernatur aut odit aut fugit, sed quia consequuntur magni dolores eos qui ratione voluptatem sequi nesciunt. Neque porro quisquam est, qui dolorem ipsum quia dolor sit amet, consectetur, adipisci velit, sed quia non numquam eius modi tempora incidunt ut labore et dolore magnam aliquam quaerat voluptatem. Ut enim ad minima veniam, quis nostrum exercitationem ullam corporis suscipit laboriosam, nisi ut aliquid ex ea commodi consequatur.Nemo enim ipsam voluptatem quia voluptas sit aspernatur aut odit aut fugit, sed quia consequuntur magni dolores eos qui ratione voluptatem sequi nesciunt. Neque porro quisquam est, qui dolorem ipsum quia dolor sit amet, consectetur, adipisci velit, sed quia non numquam eius modi tempora incidunt ut labore et dolore magnam aliquam quaerat voluptatem. Ut enim ad minima veniam, quis nostrum exercitationem ullam corporis suscipit laboriosam, nisi ut aliquid ex ea commodi consequatur Quis autem vel eum iure reprehenderit qui in ea voluptate velit esse quam nihil molestiae consequatur, vel illum qui dolorem eum fugiat quo voluptas nulla pariatur</p>
  <p class="copyright">© Copyright 2023 Tarvel Works.All rights reserved.</p>
  <p class="page-no">02</p>
</section>

<!-- Services -->
<section class="slide" style="top:1406px">
  <div class="header">
    <svg width="1149" height="56" viewBox="0 0 1149 56"><polygon points="0,0 935,0 900,56 0,56" fill="#000"/><polygon points="947,0 960,0 925,56 912,56" fill="#b9862f"/><polygon points="968,0 981,0 946,56 933,56" fill="#b9862f"/></svg>
    <h2>OUR SERVICES</h2><span class="brand">Tarvel Works</span>
  </div>
  <div class="service dark" style="left:21px"><span class="brand">Tarvel Works</span><h3>NEMO ENIM IPSAM</h3><p>Lorem ipsum dolor sit amet, consectetur adipiscing elit, sed do eiusmod tempor incididunt ut labore et dolore magna aliqua. Ut enim ad minim veniam, quis nostrud exercitation ullamco laboris nisi ut aliquip ex ea commodo consequat. Duis aute irure dolor in reprehenderit in voluptate velit esse cillum dolore eu fugiat nulla .pariatur</p><div class="go"><svg width="24" height="24" viewBox="0 0 24 24"><circle cx="12" cy="12" r="10" fill="#fff"/><path d="M7 12h8M12 8l4 4-4 4" stroke="#000" stroke-width="2.4" fill="none"/></svg></div></div>
  <div class="service gold" style="left:302px"><span class="brand">Tarvel Works</span><h3>NEMO ENIM IPSAM</h3><p>Lorem ipsum dolor sit amet, consectetur adipiscing elit, sed do eiusmod tempor incididunt ut labore et dolore magna aliqua. Ut enim ad minim veniam, quis nostrud exercitation ullamco laboris nisi ut aliquip ex ea commodo consequat. Duis aute irure dolor in reprehenderit in voluptate velit esse cillum dolore eu fugiat nulla .pariatur</p><div class="go"><svg width="24" height="24" viewBox="0 0 24 24"><circle cx="12" cy="12" r="10" fill="#fff"/><path d="M7 12h8M12 8l4 4-4 4" stroke="#000" stroke-width="2.4" fill="none"/></svg></div></div>
  <div class="service dark" style="left:583px"><span class="brand">Tarvel Works</span><h3>NEMO ENIM IPSAM</h3><p>Lorem ipsum dolor sit amet, consectetur adipiscing elit, sed do eiusmod tempor incididunt ut labore et dolore magna aliqua. Ut enim ad minim veniam, quis nostrud exercitation ullamco laboris nisi ut aliquip ex ea commodo consequat. Duis aute irure dolor in reprehenderit in voluptate velit esse cillum dolore eu fugiat nulla .pariatur</p><div class="go"><svg width="24" height="24" viewBox="0 0 24 24"><circle cx="12" cy="12" r="10" fill="#fff"/><path d="M7 12h8M12 8l4 4-4 4" stroke="#000" stroke-width="2.4" fill="none"/></svg></div></div>
  <div class="service gold" style="left:865px"><span class="brand">Tarvel Works</span><h3>NEMO ENIM IPSAM</h3><p>Lorem ipsum dolor sit amet, consectetur adipiscing elit, sed do eiusmod tempor incididunt ut labore et dolore magna aliqua. Ut enim ad minim veniam, quis nostrud exercitation ullamco laboris nisi ut aliquip ex ea commodo consequat. Duis aute irure dolor in reprehenderit in voluptate velit esse cillum dolore eu fugiat nulla .pariatur</p><div class="go"><svg width="24" height="24" viewBox="0 0 24 24"><circle cx="12" cy="12" r="10" fill="#fff"/><path d="M7 12h8M12 8l4 4-4 4" stroke="#000" stroke-width="2.4" fill="none"/></svg></div></div>
  <p class="copyright">© Copyright 2023 Tarvel Works.All rights reserved.</p>
  <p class="page-no">03</p>
</section>

<!-- Capacities -->
<section class="slide" style="top:2115px">
  <div class="header">
    <svg width="1149" height="56" viewBox="0 0 1149 56"><polygon points="0,0 935,0 900,56 0,56" fill="#000"/><polygon points="947,0 960,0 925,56 912,56" fill="#b9862f"/><polygon points="968,0 981,0 946,56 933,56" fill="#b9862f"/></svg>
    <h2>CAPACITIES AND PRESENT WORKFLOWS</h2><span class="brand">Tarvel Works</span>
  </div>
  <svg class="abs" style="left:0;top:0" width="1149" height="647" viewBox="0 0 1149 647">
    <g stroke="#555" stroke-width="1.2" stroke-dasharray="4 3" fill="none">
      <polyline points="177,143 440,143 481,218"/>
      <polyline points="170,309 415,309 431,321"/>
      <polyline points="177,483 440,483 481,440"/>
      <polyline points="979,143 710,143 671,218"/>
      <polyline points="979,309 735,309 722,321"/>
      <polyline points="979,483 710,483 671,440"/>
    </g>
    <circle cx="575" cy="321" r="146" fill="none" stroke="#555" stroke-width="3"/>
    <circle cx="481" cy="218" r="11" fill="#b9862f"/>
    <circle cx="671" cy="218" r="11" fill="#000"/>
    <circle cx="431" cy="321" r="11" fill="#000"/>
    <circle cx="722" cy="321" r="11" fill="#b9862f"/>
    <circle cx="481" cy="440" r="11" fill="#b9862f"/>
    <circle cx="671" cy="440" r="11" fill="#000"/>
  </svg>
  <div class="abs cap-center"><span class="brand">Tarvel<br>Works</span></div>

  <div class="cap-icon" style="left:93px;top:119px"><svg width="36" height="36" viewBox="0 0 36 36" fill="none" stroke="#fff" stroke-width="2"><circle cx="11" cy="12" r="4"/><circle cx="25" cy="12" r="4"/><path d="M3 30c0-6 4-10 8-10s8 4 8 10M17 30c0-6 4-10 8-10s8 4 8 10"/></svg></div>
  <div class="cap-item" style="left:177px;top:120px"><h4>NEMO ENIM IPSAM</h4><p>Lorem ipsum dolor sit amet, consectetur adipiscing elit, sed do eiusmod tempor incididunt ut labore et dolore magna aliqua. Ut enim ad minim veniam, quis nostrud exercitation ullamco laboris nisi ut aliquip ex ea commodo consequat. Duis aute irure dolor in reprehenderit in voluptate velit</p></div>

  <div class="cap-icon" style="left:88px;top:284px"><svg width="36" height="36" viewBox="0 0 36 36" fill="none" stroke="#fff" stroke-width="2"><circle cx="18" cy="11" r="6"/><path d="M6 32c0-7 5-12 12-12s12 5 12 12"/></svg></div>
  <div class="cap-item" style="left:170px;top:286px"><h4>NEMO ENIM IPSAM</h4><p>Lorem ipsum dolor sit amet, consectetur adipiscing elit, sed do eiusmod tempor incididunt ut labore et dolore magna aliqua. Ut enim ad minim veniam, quis nostrud exercitation ullamco laboris nisi ut aliquip ex ea commodo consequat. Duis aute irure</p></div>

  <div class="cap-icon" style="left:93px;top:461px"><svg width="36" height="36" viewBox="0 0 36 36" fill="none" stroke="#fff" stroke-width="2"><rect x="4" y="4" width="18" height="12" rx="2"/><circle cx="24" cy="22" r="4"/><path d="M14 34c0-6 4-8 10-8s10 2 10 8"/></svg></div>
  <div class="cap-item" style="left:177px;top:460px"><h4>NEMO ENIM IPSAM</h4><p>Lorem ipsum dolor sit amet, consectetur adipiscing elit, sed do eiusmod tempor incididunt ut labore et dolore magna aliqua. Ut enim ad minim veniam, quis nostrud exercitation ullamco laboris nisi ut aliquip ex ea commodo consequat. Duis aute irure</p></div>

  <div class="cap-icon" style="left:986px;top:119px"><svg width="36" height="36" viewBox="0 0 36 36" fill="none" stroke="#fff" stroke-width="2"><circle cx="18" cy="14" r="8"/><circle cx="18" cy="14" r="3"/><path d="M4 30h10l6-4h10"/></svg></div>
  <div class="cap-item" style="left:749px;top:120px;width:230px"><h4>NEMO ENIM IPSAM</h4><p>Lorem ipsum dolor sit amet, consectetur adipiscing elit, sed do eiusmod tempor incididunt ut labore et dolore magna aliqua. Ut enim ad minim veniam, quis nostrud exercitation ullamco laboris nisi ut aliquip ex ea commodo consequat. Duis aute irure</p></div>

  <div class="cap-icon" style="left:986px;top:284px"><svg width="36" height="36" viewBox="0 0 36 36" fill="none" stroke="#fff" stroke-width="2"><circle cx="14" cy="14" r="5"/><path d="M4 32c0-6 4-10 10-10s10 4 10 10M24 14v-8M28 14v-5M32 14v-10"/></svg></div>
  <div class="cap-item" style="left:749px;top:286px;width:230px"><h4>NEMO ENIM IPSAM</h4><p>Lorem ipsum dolor sit amet, consectetur adipiscing elit, sed do eiusmod tempor incididunt ut labore et dolore magna aliqua. Ut enim ad minim veniam, quis nostrud exercitation ullamco laboris nisi ut aliquip ex ea commodo consequat. Duis aute irure</p></div>

  <div class="cap-icon" style="left:986px;top:461px"><svg width="36" height="36" viewBox="0 0 36 36" fill="none" stroke="#fff" stroke-width="2"><circle cx="18" cy="18" r="12"/><circle cx="18" cy="18" r="6"/><path d="M18 18l12-12"/></svg></div>
  <div class="cap-item" style="left:749px;top:460px;width:230px"><h4>NEMO ENIM IPSAM</h4><p>Lorem ipsum dolor sit amet, consectetur adipiscing elit, sed do eiusmod tempor incididunt ut labore et dolore magna aliqua. Ut enim ad minim veniam, quis nostrud exercitation ullamco laboris nisi ut aliquip ex ea commodo consequat. Duis aute irure</p></div>

  <p class="copyright">© Copyright 2023 Tarvel Works.All rights reserved.</p>
  <p class="page-no">04</p>
</section>

<!-- Team -->
<section class="slide" style="top:2824px">
  <div class="header">
    <svg width="1149" height="56" viewBox="0 0 1149 56"><polygon points="0,0 935,0 900,56 0,56" fill="#000"/><polygon points="947,0 960,0 925,56 912,56" fill="#b9862f"/><polygon points="968,0 981,0 946,56 933,56" fill="#b9862f"/></svg>
    <h2>OUR TEAM</h2><span class="brand">Tarvel Works</span>
  </div>
  <div class="member gold" style="left:70px"><div class="photo" role="img" aria-label="Portrait of a smiling team member in a blue shirt"></div><h3>NEMO ENIM</h3><p>Lorem ipsum dolor sit amet, consectetur adipiscing elit, sed do eiusmod tempor incididunt ut labore et dolore magna aliqua.</p></div>
  <div class="member dark" style="left:429px"><div class="photo" role="img" aria-label="Portrait of a team member on the phone"></div><h3>NEMO ENIM</h3><p>Lorem ipsum dolor sit amet, consectetur adipiscing elit, sed do eiusmod tempor incididunt ut labore et dolore magna aliqua.</p></div>
  <div class="member gold" style="left:788px"><div class="photo" role="img" aria-label="Portrait of a team member working on a laptop"></div><h3>NEMO ENIM</h3><p>Lorem ipsum dolor sit amet, consectetur adipiscing elit, sed do eiusmod tempor incididunt ut labore et dolore magna aliqua.</p></div>
  <p class="copyright">© Copyright 2023 Tarvel Works.All rights reserved.</p>
  <p class="page-no">05</p>
</section>

<!-- Thank you -->
<section class="slide closing" style="top:3507px">
  <div class="closing-photo" role="img" aria-label="Darkened office team photo in the background"></div>
  <div class="abs closing-brand"><span class="brand">Tarvel Works</span></div>
  <div class="abs thanks-box">
    <h2>THANK YOU</h2>
    <div class="contact" style="left:39px"><div class="ring"><svg width="22" height="26" viewBox="0 0 22 26"><path d="M11 1a9 9 0 0 0-9 9c0 7 9 15 9 15s9-8 9-15a9 9 0 0 0-9-9z" fill="none" stroke="#fff" stroke-width="2"/><circle cx="11" cy="10" r="3" fill="#fff"/></svg></div>Lorem Ipsum Dummy Lorem<br>Ipsum dummy</div>
    <div class="contact" style="left:322px"><div class="ring"><svg width="24" height="24" viewBox="0 0 24 24"><path d="M5 2l4 1 1 5-3 2a13 13 0 0 0 7 7l2-3 5 1 1 4c0 2-2 3-4 3C9 22 2 15 2 6c0-2 1-4 3-4z" fill="none" stroke="#fff" stroke-width="2"/></svg></div>Phone<br>+1 555 010 2040</div>
    <div class="contact" style="left:578px"><div class="ring"><svg width="26" height="20" viewBox="0 0 26 20"><rect x="1" y="1" width="24" height="18" rx="2" fill="none" stroke="#fff" stroke-width="2"/><path d="M1 3l12 9 12-9" fill="none" stroke="#fff" stroke-width="2"/></svg></div>Email<br>info@tarvelworks.com</div>
  </div>
  <p class="copyright">© Copyright 2023 Tarvel Works.All rights reserved.</p>
  <p class="page-no">06</p>
</section>

</body>
</html>
```